Business Card Design

Looking for business card designs for a new business. there will be two cards of the same design (both lots of information below in contact info). We would like the logo diagonally across the card with the information split above and below the logo similar to sketch. happy to look at similar alternatives
Please use same colours as in logo design

Industry/Entity Type

Business

Contact Information for Business Card

Colin Marwood
mob - 0498 172 943
ph - 02 6812 4300
fax - 02 6812 4900
email - col@ridgelinetrusses.com.au
14 Larchmont Road, Yarrandel NSW 2817

Gavin Holloway
mob - 0421 830 576
ph - 02 6812 4300
fax - 02 6812 4900
email - gavin@ridgelinetrusses.com.au

```html
<!DOCTYPE html>
<html lang="en">
<head>
<meta charset="utf-8">
<title>Ridgeline Trusses – Business Cards</title>
<link href="https://fonts.googleapis.com/css2?family=Open+Sans:wght@400;600;700;800&display=swap" rel="stylesheet">
<style>
  :root {
    --teal: #0a7f7a;
    --ink: #111111;
    --paper: #ffffff;
    --card-black: #050505;
    --backdrop: #e7e4df;
  }
  * { margin: 0; padding: 0; box-sizing: border-box; }
  html, body {
    width: 1200px; height: 1150px; overflow: hidden;
    background: var(--backdrop);
    font-family: "Open Sans", Arial, sans-serif;
  }
  .canvas { position: relative; width: 1200px; height: 1150px; }

  .card {
    position: absolute;
    width: 922px; height: 525px;
    border-radius: 26px;
    overflow: hidden;
    box-shadow: 0 2px 6px rgba(0,0,0,.25);
  }
  .card--front { left: 28px; top: 25px; background: var(--paper); }
  .card--back  { left: 252px; top: 578px; background: var(--card-black); }

  .brand {
    position: absolute; left: 0; right: 0;
    display: flex; align-items: center; justify-content: center; gap: 18px;
    font-weight: 800; letter-spacing: -1px; line-height: 1;
  }
  .brand__square { width: 44px; height: 44px; background: var(--teal); }
  .card--front .brand { top: 118px; font-size: 64px; color: var(--ink); }
  .card--back .brand { top: 210px; font-size: 72px; color: var(--teal); }
  .card--back .brand__square { width: 50px; height: 50px; background: var(--paper); }

  .contact {
    position: absolute; top: 286px;
    font-size: 21px; color: var(--ink); line-height: 36px;
  }
  .contact--office { right: calc(922px - 396px); text-align: right; }
  .contact--direct { left: 428px; }
  .contact--direct .contact__email { font-size: 18px; }
  .contact__divider {
    position: absolute; left: 411px; top: 288px;
    width: 1px; height: 104px; background: #8a8a8a;
  }
  .contact__row { display: flex; align-items: center; gap: 6px; white-space: nowrap; }
  .contact--office .contact__row { justify-content: flex-end; }
  .icon { width: 18px; height: 18px; fill: var(--ink); flex: none; }

  .footer-band { position: absolute; left: 0; top: 440px; width: 922px; height: 85px; }
  .holder-name {
    position: absolute; right: 92px; top: 464px;
    font-size: 27px; font-weight: 700; color: var(--paper); letter-spacing: .3px;
  }

  .web-address {
    position: absolute; left: 0; right: 0; top: 418px;
    text-align: center; color: var(--paper);
    font-size: 27px; letter-spacing: 2.5px;
  }
  .web-address strong { font-weight: 700; }
</style>
</head>
<body>
<div class="canvas">

  <section class="card card--front" aria-label="Business card front">
    <div class="brand"><span class="brand__square"></span>Ridgeline Trusses</div>

    <div class="contact contact--office">
      <div class="contact__row">
        <svg class="icon" viewBox="0 0 24 24"><path d="M6.6 10.8a15.2 15.2 0 0 0 6.6 6.6l2.2-2.2a1 1 0 0 1 1-.25 11.4 11.4 0 0 0 3.6.57 1 1 0 0 1 1 1V20a1 1 0 0 1-1 1A17 17 0 0 1 3 4a1 1 0 0 1 1-1h3.5a1 1 0 0 1 1 1c0 1.25.2 2.45.57 3.57a1 1 0 0 1-.25 1z"/></svg>
        02 6812 4300
      </div>
      <div class="contact__row">14 Larchmont Road</div>
      <div class="contact__row">Yarrandel NSW 2817</div>
    </div>

    <div class="contact__divider"></div>

    <div class="contact contact--direct">
      <div class="contact__row">
        <svg class="icon" viewBox="0 0 24 24"><path d="M8 1h8a2 2 0 0 1 2 2v18a2 2 0 0 1-2 2H8a2 2 0 0 1-2-2V3a2 2 0 0 1 2-2zm0 3v9h8V4zm1 11v2h2v-2zm4 0v2h2v-2zm-4 3v2h2v-2zm4 0v2h2v-2z"/></svg>
        0421 830 576
      </div>
      <div class="contact__row">
        <svg class="icon" viewBox="0 0 24 24"><path d="M7 3h8v5H7zM4 9h16a2 2 0 0 1 2 2v7a2 2 0 0 1-2 2H4a2 2 0 0 1-2-2v-7a2 2 0 0 1 2-2zm2 3v2h5v-2z"/></svg>
        02 6812 4900
      </div>
      <div class="contact__row contact__email">
        <svg class="icon" viewBox="0 0 24 24"><path d="M2 9l10-6 10 6v11a1 1 0 0 1-1 1H3a1 1 0 0 1-1-1zm3 .6L12 14l7-4.4L12 5.4z"/></svg>
        gavin@ridgelinetrusses.com.au
      </div>
    </div>

    <svg class="footer-band" viewBox="0 0 922 85" aria-hidden="true">
      <polygon points="0,6 422,6 396,32 0,32" fill="var(--ink)"/>
      <polygon points="444,6 922,6 922,85 0,85 0,46 404,46" fill="var(--teal)"/>
    </svg>
    <div class="holder-name">Gavin Holloway</div>
  </section>

  <section class="card card--back" aria-label="Business card back">
    <div class="brand"><span class="brand__square"></span>Ridgeline Trusses</div>
    <div class="web-address">www.<strong>ridgelinetrusses</strong>.com.au</div>
  </section>

</div>
</body>
</html>
```